Business Card / Appointment Card for Physician

On one side it should give the logo, address, and contact information, and on the other side it should br an Appointment card.

One Side:
Logo (see attached files)
Board Certified American Orthopedic Surgery

1487 Harrowgate Ave.
Suite KM7
Bronx, NY 10527
Tel: (718) 552 - 1948
Fax: (718) 552 - 7210

628 Fourth Ave.
Suite 42
New York, NY 10087
Tel: (212) 734 - 2815

Second Side:
Appointment
give them a choice of Bronx or Mahattan office
For:
Date:
Time:

If you are unable to keep your appointment, please call (718) 263-5102 24hrs in advance.

Target Market(s)

People that need orthopedic surgery

Industry/Entity Type

Business

Contact Information for Business Card

smart and attractive

Requirements
Must have
• logo
• contact information on one side, appointment information on the other

```html
<!DOCTYPE html>
<html lang="en">
<head>
<meta charset="utf-8">
<title>Hartwell Orthopaedics – Business &amp; Appointment Card</title>
<link href="https://fonts.googleapis.com/css2?family=Roboto+Condensed:wght@400;500&family=Arimo:ital,wght@0,400;1,700&display=swap" rel="stylesheet">
<style>
  :root {
    --page-bg: #ecebe8;
    --card-white: #ffffff;
    --brand-blue: #0b6bb3;
    --ink-blue: #0a5fa8;
    --accent-green: #6cb33f;
    --field-white: #ffffff;
  }
  * { box-sizing: border-box; margin: 0; padding: 0; }
  html, body { width: 1200px; height: 1200px; overflow: hidden; }
  body {
    background: var(--page-bg);
    display: flex;
    flex-direction: column;
    align-items: center;
    justify-content: center;
    gap: 60px;
  }
  .card {
    width: 875px;
    height: 500px;
    position: relative;
    box-shadow: 0 6px 20px rgba(0,0,0,0.12);
  }

  /* Front side */
  .card--front {
    background: var(--card-white);
    padding: 40px 50px 0;
    display: flex;
    flex-direction: column;
    align-items: center;
  }
  .brand-mark {
    width: 170px;
    height: 170px;
    border-radius: 50%;
    background: var(--brand-blue);
  }
  .practice-name {
    margin-top: 18px;
    font-family: "Roboto Condensed", sans-serif;
    font-weight: 500;
    font-size: 58px;
    letter-spacing: 0.5px;
    color: var(--ink-blue);
    line-height: 1;
  }
  .practice-specialty {
    margin-top: 12px;
    font-family: "Roboto Condensed", sans-serif;
    font-size: 32px;
    color: var(--ink-blue);
    line-height: 1;
  }
  .offices {
    margin-top: 26px;
    width: 100%;
    display: grid;
    grid-template-columns: 1fr 1fr;
    gap: 30px;
    font-family: "Arimo", sans-serif;
    font-style: italic;
    font-weight: 700;
    font-size: 19px;
    line-height: 1.15;
    color: var(--ink-blue);
  }

  /* Back side */
  .card--back {
    background: var(--brand-blue);
    font-family: "Arimo", sans-serif;
    color: var(--field-white);
    padding: 60px 70px 0;
  }
  .office-choice {
    display: flex;
    gap: 150px;
    margin-left: 110px;
    font-size: 30px;
  }
  .office-option { display: flex; align-items: center; gap: 14px; }
  .checkbox {
    width: 40px;
    height: 40px;
    background: var(--field-white);
    border: 3px solid var(--accent-green);
  }
  .fields { margin-top: 34px; display: flex; flex-direction: column; gap: 22px; }
  .field { display: flex; align-items: center; gap: 18px; }
  .field-label { width: 72px; font-size: 22px; text-align: right; }
  .field-box {
    flex: 1;
    height: 50px;
    background: var(--field-white);
    border: 3px solid var(--accent-green);
  }
  .notice {
    margin-top: 40px;
    text-align: center;
    font-size: 22px;
    line-height: 1.35;
  }
</style>
</head>
<body>
  <section class="card card--front">
    <div class="brand-mark" aria-hidden="true"></div>
    <h1 class="practice-name">DANIEL R. HARTWELL MD PC</h1>
    <p class="practice-specialty">ORTHOPAEDIC SURGERY &amp; SPORTS MEDICINE</p>
    <div class="offices">
      <address class="office">
        1487 Harrowgate Ave. Suite KM7 Bronx,<br>
        NY 10527<br>
        Tel: (718) 552 - 1948<br>
        Fax: (718) 552 - 7210
      </address>
      <address class="office">
        628 Fourth Ave. Suite 42 New York,<br>
        NY 10087<br>
        Tel: (212) 734 - 2815
      </address>
    </div>
  </section>

  <section class="card card--back">
    <div class="office-choice">
      <div class="office-option"><span class="checkbox"></span>Bronx Office</div>
      <div class="office-option"><span class="checkbox"></span>Manhattan Office</div>
    </div>
    <div class="fields">
      <div class="field"><span class="field-label">For:</span><span class="field-box"></span></div>
      <div class="field"><span class="field-label">Date:</span><span class="field-box"></span></div>
      <div class="field"><span class="field-label">Time:</span><span class="field-box"></span></div>
    </div>
    <p class="notice">If you are unable to keep your appointment,<br>please call (718) 263-5102 24hrs in advance.</p>
  </section>
</body>
</html>
```